Bright Pelvic Health Business Card

Need a business card for a surgical practice called Bright Pelvic Health. We have recently selected a logo (attached). The business card will need to have two formats:
1) One with the logo/physician name/ contact info on the front and location information on the back.
2) One in "appointment reminder card" style with the logo/ contact info/ date/ time on the front and the location information on the back.

The front side should include the following information:
- Logo
- Ravi K. Desai, MD FACOG
- phone: 469-555-0182
- fax: 1-469-555-0147
- email: admin@brightpelvic.example
- website: www.brightpelvichealth.example

The back side should have the office locations listed:
4812 Quarry Bend Dr, Plano, TX 75093
3650 Wrenfield Rd, Plano, TX 75025
2245 Brambleton Ln, Irving, TX 75038
915 S Garnet Ave B314, Dallas, TX 75201
1836 Tillman Pkwy, Grand Prairie, TX 75051
6417 Dorrance Way Dr, San Antonio, TX 78240
5920 Kessler Rd, Pasadena, TX 77504

Target Market(s)

1. Other physicians who might refer patients
2. Female patients

Industry/Entity Type

Business

Font styles to use
Other font styles liked:
• Tahoma for lettering

Requirements
Must have
• As per the instructions
Should not have
• No other images needed -- please try to keep font consistent with logo design. Can use Tahoma as the font for lettering.

```html
<!DOCTYPE html>
<html lang="en">
<head>
<meta charset="UTF-8">
<title>Bright Pelvic Health – Business Card</title>
<link rel="stylesheet" href="https://fonts.googleapis.com/css2?family=PT+Sans:wght@400;700&display=swap">
<style>
  :root{
    --page:#e9ebee;
    --blue-deep:#1f5fc4;
    --blue-mid:#3f8ee0;
    --blue-light:#a9d4f5;
    --blue-pale:#d8ecfb;
    --navy:#1d3b86;
    --ink:#2a2f3a;
    --card-grey:#eeeff1;
    --rule:#c9ccd1;
    --white:#ffffff;
    --dot:#1f5fc4;
  }
  *{box-sizing:border-box;margin:0;padding:0}
  html,body{width:1200px;height:900px;overflow:hidden}
  body{
    background:var(--page);
    font-family:"PT Sans", Tahoma, sans-serif;
    color:var(--ink);
    position:relative;
  }
  .card{
    position:absolute;
    left:320px;
    width:560px;
    height:320px;
    border-radius:3px;
    overflow:hidden;
    box-shadow:0 6px 18px rgba(0,0,0,.18);
  }
  /* ---------- front ---------- */
  .card-front{
    top:90px;
    background:
      radial-gradient(ellipse at 50% 42%, var(--blue-pale) 0%, var(--blue-light) 38%, var(--blue-mid) 78%, var(--blue-deep) 100%);
  }
  .front-content{
    position:absolute;inset:0;
    display:flex;flex-direction:column;align-items:center;justify-content:center;
    text-align:center;
  }
  .wordmark{
    display:flex;align-items:center;gap:12px;
    margin-bottom:26px;
  }
  .wordmark-dot{
    width:22px;height:22px;border-radius:50%;
    background:var(--navy);
    flex:none;
  }
  .wordmark-name{
    font-weight:700;
    font-size:34px;
    color:var(--navy);
    letter-spacing:.3px;
    white-space:nowrap;
  }
  .physician{
    font-size:17px;
    color:var(--navy);
    margin-bottom:4px;
  }
  .specialty{
    font-size:16px;
    color:var(--navy);
  }
  /* ---------- back ---------- */
  .card-back{
    top:490px;
    background:var(--card-grey);
  }
  .contact-band{
    position:absolute;left:0;top:0;width:100%;height:118px;
    background:linear-gradient(100deg, var(--blue-deep) 0%, var(--blue-mid) 55%, #5fb0ea 100%);
    clip-path:polygon(0 0, 88% 0, 80% 100%, 0 100%);
  }
  .contact-grid{
    position:absolute;left:24px;top:20px;
    display:grid;
    grid-template-columns:196px 196px;
    row-gap:10px;column-gap:8px;
    color:var(--white);
    font-size:12.5px;
  }
  .contact-item{display:flex;align-items:center;gap:7px;white-space:nowrap}
  .contact-item svg{width:13px;height:13px;flex:none;fill:var(--white)}
  .contact-grid .contact-item:nth-child(odd){margin-top:22px}
  .back-mark{
    position:absolute;right:20px;top:150px;
    display:flex;align-items:center;gap:7px;
  }
  .back-mark .wordmark-dot{width:13px;height:13px}
  .back-mark .wordmark-name{font-size:15px}
  .locations{
    position:absolute;left:24px;top:128px;
    list-style:none;
    width:340px;
  }
  .locations li{
    position:relative;
    padding-left:14px;
    font-size:15px;
    line-height:25px;
    border-bottom:1px solid var(--rule);
    color:var(--ink);
    white-space:nowrap;
  }
  .locations li:last-child{border-bottom:none}
  .locations li::before{
    content:"";
    position:absolute;left:0;top:11px;
    width:5px;height:5px;border-radius:50%;
    background:var(--dot);
  }
</style>
</head>
<body>

  <section class="card card-front" aria-label="Business card front">
    <div class="front-content">
      <div class="wordmark">
        <span class="wordmark-dot"></span>
        <span class="wordmark-name">Bright Pelvic Health</span>
      </div>
      <p class="physician">Ravi K. Desai, MD FACOG</p>
      <p class="specialty">Female Pelvic Medicine &amp; Reconstructive Surgery</p>
    </div>
  </section>

  <section class="card card-back" aria-label="Business card back">
    <div class="contact-band"></div>
    <div class="contact-grid">
      <div class="contact-item">
        <svg viewBox="0 0 24 24" aria-hidden="true"><path d="M6.6 10.8a15.1 15.1 0 0 0 6.6 6.6l2.2-2.2c.3-.3.7-.4 1-.2 1.1.4 2.3.6 3.6.6.6 0 1 .4 1 1V20c0 .6-.4 1-1 1A17 17 0 0 1 3 4c0-.6.4-1 1-1h3.5c.6 0 1 .4 1 1 0 1.3.2 2.5.6 3.6.1.3 0 .7-.2 1z"/></svg>
        <span>469-555-0182</span>
      </div>
      <div class="contact-item">
        <svg viewBox="0 0 24 24" aria-hidden="true"><path d="M6 3h10v5H6zM4 9h16a2 2 0 0 1 2 2v6h-4v4H6v-4H2v-6a2 2 0 0 1 2-2zm4 7v3h8v-3z"/></svg>
        <span>1-469-555-0147</span>
      </div>
      <div class="contact-item">
        <svg viewBox="0 0 24 24" aria-hidden="true"><path d="M3 5h18v14H3zm2 2v.4l7 4.6 7-4.6V7zm0 2.8V17h14V9.8l-7 4.6z"/></svg>
        <span>admin@brightpelvic.example</span>
      </div>
      <div class="contact-item">
        <svg viewBox="0 0 24 24" aria-hidden="true"><path d="M12 2a10 10 0 1 0 0 20 10 10 0 0 0 0-20zm6.9 9h-3a15 15 0 0 0-1.3-5.9A8 8 0 0 1 18.9 11zM12 4c.9 1.3 1.7 3.7 1.9 7h-3.8c.2-3.3 1-5.7 1.9-7zM9.4 5.1A15 15 0 0 0 8.1 11h-3a8 8 0 0 1 4.3-5.9zM5.1 13h3a15 15 0 0 0 1.3 5.9A8 8 0 0 1 5.1 13zM12 20c-.9-1.3-1.7-3.7-1.9-7h3.8c-.2 3.3-1 5.7-1.9 7zm2.6-1.1a15 15 0 0 0 1.3-5.9h3a8 8 0 0 1-4.3 5.9z"/></svg>
        <span>www.brightpelvichealth.example</span>
      </div>
    </div>

    <div class="back-mark">
      <span class="wordmark-dot"></span>
      <span class="wordmark-name">Bright Pelvic Health</span>
    </div>

    <ul class="locations">
      <li>4812 Quarry Bend Dr, Plano, TX 75093</li>
      <li>3650 Wrenfield Rd, Plano, TX 75025</li>
      <li>2245 Brambleton Ln, Irving, TX 75038</li>
      <li>915 S Garnet Ave B314, Dallas, TX 75201</li>
      <li>1836 Tillman Pkwy, Grand Prairie, TX 75051</li>
      <li>6417 Dorrance Way Dr, San Antonio, TX 78240</li>
      <li>5920 Kessler Rd, Pasadena, TX 77504</li>
    </ul>
  </section>

</body>
</html>
```